Thai Takeaway Menu Design

I need a menu re-design for a thai takeaway/restaurant in australia.

Please use content from the existing menu
http://www.platterwink.example/u/menu/7302918?p=1

I'd like to emphasise on
1 - free delivery for order over $40
2 - gluten free and vegetatian option available on most meal (however you want to word it - not fuss)

*remove (the banner order online and save $10)

I'm happy to change the whole concept & design. I particularly like rustic, raw look more than moden ones. Does not need to be flowery or anything like current one :)

Industry/Entity Type

Restaurant

```html
<!DOCTYPE html>
<html lang="en">
<head>
<meta charset="utf-8">
<title>Ruen Baan – Takeaway Menu</title>
<link rel="stylesheet" href="https://fonts.googleapis.com/css2?family=Tinos:wght@400;700&family=Orbitron:wght@500&display=swap">
<style>
  :root {
    --backdrop: #ececec;
    --panel: #2a2a2c;
    --panel-edge: #1f1f21;
    --red: #e3202a;
    --red-dark: #8e0d12;
    --red-text: #ee2730;
    --ink: #f4f4f4;
  }
  * { box-sizing: border-box; margin: 0; padding: 0; }
  html, body { width: 1200px; height: 900px; overflow: hidden; }
  body {
    background: var(--backdrop);
    font-family: "Tinos", "Times New Roman", serif;
    color: var(--ink);
    position: relative;
  }
  .menu {
    position: absolute; left: 90px; top: 100px;
    display: flex; width: 1020px; height: 700px;
    box-shadow: 0 12px 30px rgba(0,0,0,.25);
  }
  .panel {
    position: relative; width: 340px; height: 100%;
    background: var(--panel);
    border-right: 1px solid var(--panel-edge);
  }
  .panel:last-child { border-right: 0; }
  .ribbon {
    display: block; margin: 0 auto; width: 250px; height: 52px;
    border-radius: 10px;
    background: linear-gradient(180deg, var(--red) 0%, var(--red-dark) 100%);
    font-weight: 700; font-size: 27px; line-height: 52px; text-align: center;
    color: #fff;
  }
  .ribbon--small { width: 210px; height: 46px; line-height: 46px; font-size: 22px; }
  .dishes { list-style: none; font-weight: 700; font-size: 18px; line-height: 28px; padding-left: 45px; margin-top: 18px; position: relative; }
  .dishes--light { font-weight: 400; font-size: 15px; line-height: 27px; padding-left: 40px; }
  .price { position: absolute; right: 40px; bottom: 0; color: var(--red-text); font-weight: 700; font-size: 32px; line-height: 36px; }
  .price--small { font-size: 24px; bottom: 24px; right: 45px; }
  .note { font-size: 11px; line-height: 14px; }
  .service { color: var(--red-text); font-weight: 700; font-size: 19px; text-align: center; }
  .service--bottom { position: absolute; left: 0; right: 0; bottom: 140px; }
  .tagline { font-family: "Orbitron", sans-serif; color: var(--red-text); text-align: center; letter-spacing: 1px; }
  .hours, .address { text-align: center; font-weight: 700; }
  .footer-band {
    position: absolute; left: 0; right: 0; bottom: 50px; height: 44px;
    background: linear-gradient(180deg, var(--red) 0%, var(--red-dark) 100%);
    font-size: 13px; line-height: 15px; display: flex; align-items: center; padding-left: 30px;
  }
  .seal {
    position: absolute; right: 30px; top: 50%; transform: translateY(-50%);
    width: 62px; height: 62px; border-radius: 50%;
    background: var(--red); border: 3px solid var(--panel);
    box-shadow: 0 0 0 2px var(--red);
    display: flex; align-items: center; justify-content: center;
    font-weight: 700; font-size: 26px; color: #fff;
  }
  .seal-square { width: 22px; height: 22px; background: var(--panel); border-radius: 3px; }
  .brand { color: var(--red-text); font-weight: 700; text-align: center; }
</style>
</head>
<body>
<main class="menu">
  <section class="panel panel--packs">
    <div style="height:48px"></div>
    <h2 class="ribbon">Dinner for Two</h2>
    <ul class="dishes">
      <li>Spring Rolls (4)</li>
      <li>Chiken &amp; Cashew Nuts</li>
      <li>Massaman curry</li>
      <li>Rice</li>
      <li class="price">$28</li>
    </ul>
    <div style="height:60px"></div>
    <h2 class="ribbon">Family Pack</h2>
    <ul class="dishes">
      <li>Spring rolls (4)</li>
      <li>Satay Chicken(4)</li>
      <li>Chicken &amp; Cashew nut</li>
      <li>Pad Thai</li>
      <li>Rice (L)</li>
      <li class="price">$45</li>
    </ul>
    <p class="service service--bottom">Dine in, Take away &amp; Delivery</p>
    <div class="footer-band">Vegeterian OptionsAvailable<br>&nbsp;&nbsp;&nbsp;on Most of the Meals
      <span class="seal"><span class="seal-square"></span></span>
    </div>
  </section>

  <section class="panel panel--lunch">
    <div style="height:55px"></div>
    <h2 class="ribbon ribbon--small">Lunch Special</h2>
    <ul class="dishes dishes--light">
      <li>Pad thai</li>
      <li>Sweet and sour pork /w Rice</li>
      <li>Chicken &amp; Cashew Nut /w Rice</li>
      <li>Green Curry Chicken /w Rice</li>
      <li>Beef noodle Soup</li>
      <li class="note">(Free can of Soft Drink)</li>
      <li class="price price--small">$10</li>
    </ul>
    <p class="hours" style="font-weight:400;font-size:11px;line-height:14px;margin-top:50px">Trading Hours<br>Lunch(Wednesday-Sunday);11.00-2.30PM<br>Dinner (7 days):5.00-9.30PM</p>
    <p class="brand" style="font-size:22px;margin-top:45px">Ruen Baan</p>
    <p class="tagline" style="font-size:11px;margin-top:25px">Traditional Thai Cusine</p>
    <p class="address" style="font-weight:400;font-size:12px;line-height:15px;margin-top:25px">62 Calloway road.Ashgrove,<br>Corner of Lark St.and Calloway Rd.<br>Phone :0755501847</p>
    <div class="footer-band">Gluten Free
      <span class="seal"></span>
    </div>
  </section>

  <section class="panel panel--cover">
    <div style="height:120px"></div>
    <h1 class="brand" style="font-size:56px;line-height:64px">Ruen Baan</h1>
    <div style="height:110px"></div>
    <p class="tagline" style="font-size:16px">Traditional Thai Cusine</p>
    <p class="hours" style="font-size:14px;line-height:17px;margin-top:30px">Trading Hours<br>Lunch(Wednesday-Sunday);11.00-2.30PM<br>Dinner (7 days):5.00-9.30PM</p>
    <p class="service" style="font-size:18px;margin-top:32px">Dine in, Take away &amp; Delivery</p>
    <p class="address" style="font-size:14px;line-height:17px;margin-top:32px">62 Calloway road.Ashgrove,<br>Corner of Lark St.and Calloway Rd.<br>Phone :0755501847</p>
    <div class="footer-band">Free delivery with in 5km<br>&nbsp;&nbsp;&nbsp;&nbsp;&nbsp;&nbsp;Minimum order
      <span class="seal">$40</span>
    </div>
  </section>
</main>
</body>
</html>
```